Flier redesign 2021

The 3 prior year fliers are attached. We want a new design for 2021 -

* DO NOT SIMPLY COPY and change the year.
*All text should be the same, except year is 2021.
*Use different photos. You can find photos on our website maplecrestgardens.org or on our google page.

Requirements
Must have
• MUST be done in photoshop an photoshop file must be provided at the end.
Should not have
• Should not be same design as previous years.

```html
<!DOCTYPE html>
<html lang="en">
<head>
<meta charset="utf-8">
<title>Maplecrest Gardens – 2021 Landscape Packages</title>
<link href="https://fonts.googleapis.com/css2?family=Poppins:wght@300;600;700&family=Noto+Serif:wght@400;700&family=Playfair+Display:wght@700&display=swap" rel="stylesheet">
<style>
  :root {
    --crimson: #8c1d22;
    --crimson-dark: #7f181d;
    --ink: #2a2a2a;
    --paper: #ffffff;
    --stage: #ffffff;
    --rule: #dcb4b4;
    --column-edge: #e4e4e4;
    --gold: #b8892c;
    --photo-top: #3a2c1a;
    --photo-mid: #5a4a36;
    --photo-low: #8c6a3e;
    --photo-base: #a47b46;
  }
  * { box-sizing: border-box; margin: 0; padding: 0; }
  html, body { width: 1200px; height: 1200px; overflow: hidden; background: var(--stage); }
  .flyer {
    position: absolute; left: 214px; top: 98px;
    width: 774px; height: 1002px;
    background: var(--paper);
    overflow: hidden;
    font-family: "Noto Serif", Georgia, serif;
    color: var(--ink);
  }
  .hero-photo {
    position: absolute; left: 0; top: 0; width: 100%; height: 664px;
    background: linear-gradient(180deg, var(--photo-top) 0%, #4b3920 25%, var(--photo-mid) 45%, var(--photo-low) 72%, var(--photo-base) 100%);
  }
  .brand {
    position: absolute; left: 332px; top: 0; width: 111px; height: 156px;
    background: var(--paper);
    display: flex; flex-direction: column; align-items: center; justify-content: flex-end;
    padding-bottom: 14px; gap: 8px;
  }
  .brand-mark { width: 46px; height: 46px; border: 2px solid var(--crimson); }
  .brand-name {
    font-family: "Noto Serif", Georgia, serif; color: var(--crimson);
    font-size: 15px; line-height: 1.15; text-align: center;
  }
  .title {
    position: absolute; left: 65px; top: 294px; width: 637px; height: 54px;
    border-top: 1px solid rgba(255,255,255,.85); border-bottom: 1px solid rgba(255,255,255,.85);
    display: flex; align-items: center; justify-content: center;
    font-family: "Poppins", Arial, sans-serif; font-weight: 300;
    font-size: 42px; letter-spacing: .5px; color: #fff; white-space: nowrap;
  }
  .package {
    position: absolute; bottom: 0;
    background: var(--paper);
    text-align: center;
    border-left: 1px solid var(--column-edge); border-right: 1px solid var(--column-edge);
  }
  .package.seasonal { left: 14px; width: 236px; top: 502px; }
  .package.perpetual { left: 270px; width: 234px; top: 376px; }
  .package.basic { left: 515px; width: 241px; top: 502px; }
  .package-name {
    font-family: "Poppins", Arial, sans-serif; font-weight: 700;
    color: var(--crimson); font-size: 22px; line-height: 1.1;
    margin-top: 24px;
  }
  .package-tagline { font-weight: 700; font-size: 13.5px; line-height: 1.15; margin-top: 22px; }
  .perpetual .package-tagline, .basic .package-tagline { margin-top: 24px; }
  .features { list-style: none; margin-top: 34px; padding: 0 12px; }
  .perpetual .features, .basic .features { margin-top: 30px; }
  .features li { font-size: 11.5px; line-height: 1.25; padding: 8px 0; }
  .features li + li { border-top: 1px solid var(--rule); }
  .features li:first-child { padding-top: 0; }
  .pricing { position: absolute; left: 0; right: 0; }
  .seasonal .pricing, .basic .pricing { top: 288px; }
  .perpetual .pricing { top: 414px; }
  .terms { display: flex; justify-content: center; gap: 34px; font-size: 12px; }
  .prices { display: flex; justify-content: center; gap: 8px; margin-top: 10px; }
  .price {
    font-family: "Playfair Display", Georgia, serif; font-weight: 700;
    font-variant-numeric: lining-nums;
    color: var(--crimson); font-size: 30px; line-height: 1;
  }
  .price.large { font-size: 42px; margin-top: 8px; }
  .price-label { font-size: 12px; }
  .price-note { font-size: 12px; line-height: 1.25; margin-top: 10px; }
  .seasonal .price-note { margin-top: 12px; }
  .badge {
    position: absolute; left: 479px; top: 419px; width: 58px; height: 58px;
    border-radius: 50%; background: radial-gradient(circle at 35% 30%, #d8ae4f, var(--gold) 60%, #8a6419);
    display: flex; align-items: center; justify-content: center; text-align: center;
    font-family: "Noto Serif", Georgia, serif; font-weight: 700;
    font-size: 6px; line-height: 1.2; color: #fff; transform: rotate(-12deg);
  }
  .footer-band {
    position: absolute; left: 0; top: 943px; width: 100%; height: 36px;
    background: var(--crimson-dark);
    color: #fff; font-size: 13px;
  }
  .footer-band span { position: absolute; top: 0; line-height: 36px; text-align: center; white-space: nowrap; }
  .footer-phone { left: 14px; width: 236px; }
  .footer-address { left: 250px; width: 274px; }
  .footer-web { left: 515px; width: 241px; }
</style>
</head>
<body>
  <main class="flyer">
    <div class="hero-photo" role="img" aria-label="Photo of an autumn cemetery path with rows of headstones under golden trees"></div>

    <div class="brand">
      <span class="brand-mark"></span>
      <span class="brand-name">Maplecrest<br>Gardens</span>
    </div>

    <h1 class="title">2021 LANDSCAPE PACKAGES</h1>

    <section class="package seasonal">
      <h2 class="package-name">SEASONAL CARE</h2>
      <p class="package-tagline">Seasonal landscaping<br>grave care.</p>
      <ul class="features">
        <li>Weeding and trimming services on<br>your gravesite approximately every<br>7 weeks during the growing<br>Season: mid-April through<br>mid-October</li>
      </ul>
      <div class="pricing">
        <div class="terms"><span>3 Years</span><span>2 Years</span><span>1 Years</span></div>
        <div class="prices"><span class="price">$357</span><span class="price">$238</span><span class="price">$119</span></div>
        <p class="price-note">Multi-year payment locks<br>in current rates.<br>Valid through 10/31/2021</p>
      </div>
    </section>

    <section class="package perpetual">
      <h2 class="package-name">PERPETUAL CARE<br>ENDOWMENT</h2>
      <p class="package-tagline">Landscaping care forever for<br>graves with plantings.</p>
      <ul class="features">
        <li>Weeding and trimming services on<br>your gravesite approximately every<br>7 weeks during the growing season:<br>mid-April through mid-October</li>
        <li>Monument leveling and cleaning</li>
        <li>Payment ensures grave care forever</li>
        <li>Full bed of boxwood shrubs</li>
        <li>Replacement of shrubs</li>
        <li>Trust certificate</li>
      </ul>
      <div class="pricing">
        <p class="price-label">12 Monthly Payments of</p>
        <p class="price large">$313</p>
        <p class="price-note">Call for single payment discount.<br>Valid through 10/31/2021</p>
      </div>
    </section>

    <span class="badge">MOST<br>POPULAR<br>PACKAGE</span>

    <section class="package basic">
      <h2 class="package-name">BASIC CARE<br>ENDOWMENT</h2>
      <p class="package-tagline">Landscaping care forever for<br>graves with no plantings.</p>
      <ul class="features">
        <li>Weeding and trimming services on<br>your gravesite 2 times per year:<br>mid-May and mid-September</li>
        <li>Monument leveling</li>
        <li>Payment ensures grave care forever</li>
      </ul>
      <div class="pricing">
        <p class="price-label">12 Monthly Payments of</p>
        <p class="price large">$255</p>
        <p class="price-note">Call for single payment discount.<br>Valid through 10/31/2021</p>
      </div>
    </section>

    <footer class="footer-band">
      <span class="footer-phone">(201) 555-0148</span>
      <span class="footer-address">48 Orchard Ave. Fairview NJ 07022</span>
      <span class="footer-web">maplecrestgardens.org</span>
    </footer>
  </main>
</body>
</html>
```